Grand Opening Banner needed for Marvelous Carpets and Home

My website is www.MarvelousCarpetsandHome.com (login with password 'plorka')

A full page banner 1000px X 500px with bright, lively colors and wording that shows an exciting GRAND OPENING celebration throughout the site. Banner needs to convey the following...

Grand Opening Sale
Runs through end of the month
Savings in every department
30 day Returns
Free Rug Pads with every rug
Free shipping.

Banner can be a simple background with graphics and text, or can be a room scene with rugs and furniture, or a grouping of rugs with text.

Some Ideas and Images can be taken from our vendor's websites, such as:

http://tbvendora.com/
http://dosmir.com/dosmir_2015/
http://www.pqmats.com/
http://zaverto.com/
http://shopbelwyn.com/

I also have quite a few room scene images available for use, if you desire.

Target Market(s)

Affluent women who care about stylish decor for their homes

Industry/Entity Type

Home And Garden

Requirements
Must have
• bold, vibrant appearance. Text that can be modified in Photoshop.
Nice to have
• HAND DRAWN, ARTIST STYLE ARTWORK IS GREATLY APPRECIATED.
• flat graphics and text with little to no 3 dimensional (shadow) effect. Font styles should be elegant/luxurious. An organic, scribbled, or painted style is nice in keeping with the handmade products that we sell.
• I am open to changing the color scheme of the website, to match your banner, so don't feel tied down to my existing colors.
Should not have
• nothing too modern or extreme in style.

```html
<!DOCTYPE html>
<html lang="en">
<head>
<meta charset="utf-8">
<title>Grand Opening Sale Banner</title>
<link rel="stylesheet" href="https://fonts.googleapis.com/css2?family=Oswald:wght@300;400&family=Cinzel:wght@400&family=Arimo:wght@400&display=swap">
<style>
  :root {
    --paper-light: #f4f4f4;
    --paper-mid: #e2e2e2;
    --paper-dark: #cfcfcf;
    --ribbon: #7a4a1e;
    --ribbon-dark: #5f3714;
    --ribbon-line: rgba(255,255,255,0.75);
    --headline: #ffffff;
    --subline: #3a3a3a;
    --perk-text: #8c1c1c;
    --perk-icon: #9b1f1f;
    --room-warm: #b07a45;
    --room-deep: #4a2a1a;
    --room-rug: #c9b898;
  }
  html, body {
    margin: 0;
    padding: 0;
    overflow: hidden;
    background: #ffffff;
  }
  .banner {
    position: relative;
    width: 1200px;
    height: 600px;
    overflow: hidden;
    background: radial-gradient(ellipse at 70% 35%, var(--paper-light) 0%, var(--paper-mid) 60%, var(--paper-dark) 100%);
  }
  .banner__art {
    position: absolute;
    inset: 0;
  }
  .headline {
    position: absolute;
    left: 390px;
    top: 88px;
    width: 732px;
    height: 104px;
    margin: 0;
    display: flex;
    align-items: center;
    justify-content: center;
    font-family: 'Oswald', sans-serif;
    font-weight: 300;
    font-size: 78px;
    letter-spacing: 1.5px;
    color: var(--headline);
    line-height: 1;
  }
  .subline {
    position: absolute;
    left: 386px;
    top: 202px;
    width: 740px;
    margin: 0;
    text-align: center;
    font-family: 'Cinzel', serif;
    font-size: 33px;
    letter-spacing: 1.5px;
    color: var(--subline);
  }
  .perks {
    list-style: none;
    margin: 0;
    padding: 0;
  }
  .perk {
    position: absolute;
    display: flex;
    align-items: center;
    gap: 13px;
    font-family: 'Arimo', sans-serif;
    font-size: 22.5px;
    letter-spacing: 1.7px;
    word-spacing: 6px;
    color: var(--perk-text);
    white-space: nowrap;
  }
  .perk__icon {
    width: 30px;
    height: 30px;
    flex: none;
  }
  .perk--savings  { left: 551px; top: 322px; }
  .perk--returns  { left: 631px; top: 379px; }
  .perk--pads     { left: 706px; top: 439px; }
  .perk--shipping { left: 777px; top: 495px; }
</style>
</head>
<body>
<main class="banner">
  <svg class="banner__art" width="1200" height="600" viewBox="0 0 1200 600">
    <defs>
      <linearGradient id="room-tone" x1="0" y1="0" x2="1" y2="1">
        <stop offset="0" stop-color="var(--room-warm)"/>
        <stop offset="0.45" stop-color="#7d5332"/>
        <stop offset="0.7" stop-color="var(--room-rug)"/>
        <stop offset="1" stop-color="var(--room-deep)"/>
      </linearGradient>
    </defs>
    <polygon class="room-photo" role="img" aria-label="Living room with a tan sofa, dark coffee table and a striped beige and grey area rug on a wooden floor" points="0,0 258,0 836,600 0,600" fill="url(#room-tone)"/>
    <line class="room-edge" x1="258" y1="0" x2="836" y2="600" stroke="#ffffff" stroke-width="3"/>
    <g class="ribbon">
      <polygon points="360,82 1152,82 1120,140 1152,198 360,198 392,140" fill="var(--ribbon)"/>
      <line x1="392" y1="92" x2="1120" y2="92" stroke="var(--ribbon-line)" stroke-width="1.5"/>
      <line x1="392" y1="188" x2="1120" y2="188" stroke="var(--ribbon-line)" stroke-width="1.5"/>
    </g>
  </svg>

  <h1 class="headline">GRAND OPENING SALE</h1>
  <p class="subline">Runs through end of the month</p>

  <ul class="perks">
    <li class="perk perk--savings">
      <svg class="perk__icon" viewBox="0 0 30 30" aria-hidden="true"><circle cx="15" cy="15" r="12" fill="var(--perk-icon)"/><circle cx="15" cy="15" r="4" fill="#ffffff"/></svg>
      Savings in every department
    </li>
    <li class="perk perk--returns">
      <svg class="perk__icon" viewBox="0 0 30 30" aria-hidden="true"><circle cx="15" cy="15" r="12" fill="var(--perk-icon)"/><circle cx="15" cy="15" r="4" fill="#ffffff"/></svg>
      30 day Returns
    </li>
    <li class="perk perk--pads">
      <svg class="perk__icon" viewBox="0 0 30 30" aria-hidden="true"><circle cx="15" cy="15" r="12" fill="var(--perk-icon)"/><circle cx="15" cy="15" r="4" fill="#ffffff"/></svg>
      Free Rug Pads with every rug
    </li>
    <li class="perk perk--shipping">
      <svg class="perk__icon" viewBox="0 0 30 30" aria-hidden="true"><circle cx="15" cy="15" r="12" fill="var(--perk-icon)"/><circle cx="15" cy="15" r="4" fill="#ffffff"/></svg>
      Free shipping
    </li>
  </ul>
</main>
</body>
</html>
```